New Creative Busines Card

Hi Lead Designer,

How are you going?

I was hoping you can help me design the perfect business card for my new business. I have listed below some background information about the business and the concept to help with your design. I'm open to any form of creative ideas, but would like to have two types of colour schemes one dark color and one light.

I would like to have a dark set of design and a light (One design with one in black or dark background and one with light background to compare the contrast since the business card will be double sided one) I imagine this will be pretty easy to change the background of the design. Would prefer one side to have all the details and the other will just have a amazing logo (K7) to give it the finishing touch.

Feel free to email me if you have any questions.

Business Structure and design concepts:

Name of the business: K7 Advisory
Business: Dating agency and event management (Date night etc)
Concept: The main focus will be the K7 ( As some sort of a heart shape like logo) be creative
Details to include in the card will be general details like Name, Title: , Email, mobile, website (Contact details will be given later).

The rest of the idea is up to you, feel free to go crazy with your creative ideas.

Thank you for your help in advance, may the best candidate win~!

Target Market(s)

Target market will be Professional, Elegant, young and ambitious people.

Industry/Entity Type

Business

Requirements
Must have
• Focus on the K7 (as some sort of a heart shape logo). Since this is a double sides design would prefer on one side to focus on the just the K7 logo and the other side with a smaller version of the logo (with it or without) and all the details such as Name, Title, Mobile, Email, Website. Please have the design in landscape format.Not fuss with the Font as long as it is easy to read.
Nice to have
• Different Contrast in colours (keep it simple) one side dark colour scheme and one side light. Prefer to have 3-4 colours (not overwhelm with too many colours) to keep it simple and elegant.
Should not have
• Too colours, main focus is should be the K7 logo not the colours

```html
<!DOCTYPE html>
<html lang="en">
<head>
<meta charset="utf-8">
<title>K7 Advisory Business Card</title>
<link rel="stylesheet" href="https://fonts.googleapis.com/css2?family=Questrial&family=Saira+Condensed:wght@400;600;700&display=swap">
<style>
  :root {
    --stage-center: #00f8ff;
    --stage-edge: #d8ffff;
    --card-dark: #0c111b;
    --card-light: #ffffff;
    --ink: #111111;
    --magenta: #ee10c6;
    --white: #ffffff;
  }
  * { margin: 0; padding: 0; box-sizing: border-box; }
  html, body { width: 1200px; height: 987px; overflow: hidden; }
  body {
    position: relative;
    background: radial-gradient(ellipse 62% 60% at 50% 48%, var(--stage-center) 0%, #5ffcff 55%, var(--stage-edge) 100%);
    font-family: "Saira Condensed", "Arial Narrow", sans-serif;
  }
  .card { position: absolute; width: 667px; height: 393px; }
  .card--front { left: 291px; top: 84px; background: var(--card-dark); }
  .card--back { left: 296px; top: 503px; background: var(--card-light); }

  .brand-mark {
    position: absolute;
    border-radius: 50%;
    background: #000;
    border: 6px solid var(--magenta);
    display: flex; align-items: center; justify-content: center;
    color: var(--white);
    font-family: "Saira Condensed", "Arial Narrow", sans-serif;
    font-weight: 700;
    line-height: 1;
  }
  .brand-mark--large { width: 234px; height: 234px; left: 217px; top: 78px; font-size: 150px; }
  .brand-mark--small { width: 84px; height: 84px; left: 290px; top: 42px; border-width: 3px; font-size: 54px; }

  .side-rule { position: absolute; width: 8px; background: var(--magenta); }
  .side-rule--left-top { left: 28px; top: 0; height: 264px; }
  .side-rule--left-bottom { left: 28px; top: 272px; height: 121px; }
  .side-rule--right-top { left: 627px; top: 0; height: 264px; }
  .side-rule--right-bottom { left: 627px; top: 272px; height: 121px; }

  .company-name {
    position: absolute; left: 0; width: 100%; top: 126px;
    text-align: center;
    font-family: "Questrial", sans-serif;
    font-size: 30px; color: var(--ink); letter-spacing: 0.5px;
  }
  .person-name {
    position: absolute; left: 0; width: 100%; top: 162px;
    text-align: center;
    font-weight: 700; font-size: 62px; line-height: 1; color: var(--ink);
  }
  .person-name .first { color: var(--magenta); }
  .person-title {
    position: absolute; left: 0; width: 100%; top: 224px;
    text-align: center;
    font-weight: 400; font-size: 27px; line-height: 1; color: var(--ink);
  }
  .person-title .accent { color: var(--magenta); }

  .contact { position: absolute; top: 268px; width: 220px; text-align: center; }
  .contact svg { display: block; margin: 0 auto; fill: var(--magenta); }
  .contact-value {
    display: block; margin-top: 14px;
    font-weight: 700; font-size: 23px; line-height: 1; color: var(--ink);
  }
  .contact--phone { left: -6px; }
  .contact--email { left: 222px; }
  .contact--web { left: 420px; }
</style>
</head>
<body>
  <section class="card card--front">
    <div class="brand-mark brand-mark--large">K7</div>
  </section>

  <section class="card card--back">
    <div class="side-rule side-rule--left-top"></div>
    <div class="side-rule side-rule--left-bottom"></div>
    <div class="side-rule side-rule--right-top"></div>
    <div class="side-rule side-rule--right-bottom"></div>

    <div class="brand-mark brand-mark--small">K7</div>
    <p class="company-name">K7 Advisory</p>
    <h1 class="person-name"><span class="first">Daniel</span> Reyes</h1>
    <p class="person-title">General <span class="accent">Manager</span></p>

    <div class="contact contact--phone">
      <svg width="22" height="42" viewBox="0 0 22 42" aria-hidden="true">
        <path d="M3 6h16a3 3 0 0 1 3 3v30a3 3 0 0 1-3 3H3a3 3 0 0 1-3-3V9a3 3 0 0 1 3-3zM15 0h3v6h-3z"/>
        <rect x="4" y="10" width="14" height="11" fill="#fff"/>
        <g fill="#fff">
          <rect x="4" y="25" width="3" height="3"/><rect x="9.5" y="25" width="3" height="3"/><rect x="15" y="25" width="3" height="3"/>
          <rect x="4" y="30" width="3" height="3"/><rect x="9.5" y="30" width="3" height="3"/><rect x="15" y="30" width="3" height="3"/>
          <rect x="4" y="35" width="3" height="3"/><rect x="9.5" y="35" width="3" height="3"/><rect x="15" y="35" width="3" height="3"/>
        </g>
      </svg>
      <span class="contact-value">0198765432</span>
    </div>

    <div class="contact contact--email">
      <svg width="56" height="38" viewBox="0 0 56 38" aria-hidden="true">
        <path d="M0 0h56v38H0z"/>
        <path d="M2 2l26 21L54 2M2 36l19-17M54 36L35 19" fill="none" stroke="#fff" stroke-width="2.5"/>
      </svg>
      <span class="contact-value" style="margin-top:12px">dreyes@k7.com</span>
    </div>

    <div class="contact contact--web">
      <svg width="40" height="40" viewBox="0 0 40 40" aria-hidden="true" fill="none" stroke="#ee10c6" stroke-width="2.5">
        <circle cx="20" cy="20" r="17"/>
        <ellipse cx="20" cy="20" rx="7" ry="17"/>
        <path d="M20 3v34M3 20h34M6 11h28M6 29h28"/>
      </svg>
      <span class="contact-value" style="margin-top:8px">k7advisory.com</span>
    </div>
  </section>
</body>
</html>
```